Golden Meadow Kit Social Media Graphics

Focusing on the Golden Meadow Kit product (3 product bundle), create 6-7 individual social media graphics (square size). For the color scheme of the graphics, they should all be complementary with the Golden Meadow Kit bottle colors.

Note: each graphic should have one of the pictures of the bottles (3-product bundle) on it and/or one of the images with a person on it (several pics attached to choose from). I even included some real customer “before and afters” pictures…you can use them if you think the quality is good enough.

Target Market(s)

men and women looking for fast, healthy loss

Industry/Entity Type

health and wellness

Requirements
Must have
• the product is a picture of ALL 3 bottles; no single bottles will be selected

```html
<!DOCTYPE html>
<html lang="en">
<head>
<meta charset="utf-8">
<title>Golden Meadow Kit – Social Graphics Board</title>
<link href="https://fonts.googleapis.com/css2?family=Red+Hat+Display:wght@500;600&display=swap" rel="stylesheet">
<style>
  :root{
    --board:#a3a3a3;
    --ink:#1d1a1f;
    --pink-1:#fbd9ec;
    --pink-2:#fff6fb;
    --ring:#b5477a;
    --blue:#2b4fb5;
    --blue-dark:#1c3a94;
    --red:#c8202f;
    --purple:#9a52c2;
    --purple-light:#b872d6;
    --white:#ffffff;
    --tick:#d42a3a;
  }
  *{box-sizing:border-box;margin:0;padding:0}
  html,body{width:1200px;height:1140px;overflow:hidden;background:var(--board)}
  body{position:relative;font-family:"Red Hat Display",sans-serif;color:var(--ink)}

  .ad{position:absolute;width:285px;height:285px;overflow:hidden;
      background:linear-gradient(160deg,var(--pink-1) 0%,var(--pink-2) 45%,var(--white) 70%)}
  .ad--1{left:141px;top:100px}
  .ad--2{left:455px;top:100px}
  .ad--3{left:774px;top:100px}
  .ad--4{left:141px;top:427px}
  .ad--5{left:455px;top:427px}
  .ad--6{left:769px;top:427px}
  .ad--7{left:141px;top:754px}

  .headline{position:absolute;left:17px;top:13px;font-weight:600;font-size:21.5px;line-height:25.5px;letter-spacing:-.3px;white-space:nowrap;z-index:2}
  .headline--tall{left:18px;top:22px;font-size:24.5px;line-height:29px}
  .headline--compact{left:18px;top:14px;font-size:21.5px;line-height:24px}

  .bottles{position:absolute;left:16px;top:100px;width:106px;height:66px;border-radius:6px;
           background:linear-gradient(90deg,#e6ecf7 0 31%,transparent 31% 34%,#efe0ee 34% 65%,transparent 65% 68%,#f4e5ea 68%)}
  .bottles--low{top:108px}

  .photo{position:absolute;width:144px;height:144px;border-radius:50%;
         box-shadow:0 0 0 3px var(--white),0 0 0 4px var(--ring)}
  .photo--before-after-a{left:130px;top:83px;background:linear-gradient(90deg,#4a3a3a 0 50%,#6c5a52 50%)}
  .photo--before-after-b{left:134px;top:89px;background:linear-gradient(90deg,#5d5548 0 52%,#6f7a4d 52%)}
  .photo--waist{left:134px;top:91px;background:radial-gradient(circle at 55% 45%,#c79a7c 0 30%,#f2efee 60%)}
  .photo--fitness{left:133px;top:89px;background:radial-gradient(circle at 60% 45%,#8a5a40 0 28%,#eeeeee 60%)}
  .photo--before-after-c{left:138px;top:90px;background:linear-gradient(90deg,#4b4f55 0 48%,#6b8660 48%)}

  .feature{position:absolute;width:285px;height:285px;left:0;top:0}

  .bullets{position:absolute;left:16px;list-style:none;font-size:5.8px;line-height:7px;font-weight:500}
  .bullets--list{top:179px}
  .bullets--list li{display:flex;align-items:center;gap:4px;height:13px}
  .bullets--grid{top:189px;display:grid;grid-template-columns:60px 60px;row-gap:6px}
  .bullets--grid li{display:flex;align-items:flex-start;gap:4px}
  .icon{flex:none;width:9px;height:9px;border-radius:50%}
  .icon--blue{background:var(--blue-dark)}
  .icon--pink{background:#d67aa5}
  .icon--red{background:var(--tick)}
  .tick{flex:none;width:8px;height:8px}

  .wave{position:absolute;left:0;top:0;width:285px;height:285px}
</style>
</head>
<body>

<svg width="0" height="0" style="position:absolute">
  <defs>
    <linearGradient id="purpleBand" x1="0" x2="1"><stop offset="0" stop-color="#8f4cba"/><stop offset="1" stop-color="#b872d6"/></linearGradient>
    <linearGradient id="blueBand" x1="0" x2="1"><stop offset="0" stop-color="#1c3a94"/><stop offset="1" stop-color="#3a63cc"/></linearGradient>
    <linearGradient id="redBand" x1="0" x2="1"><stop offset="0" stop-color="#e03a48"/><stop offset="1" stop-color="#b01a28"/></linearGradient>
    <linearGradient id="skin" x1="0" x2="0" y1="0" y2="1"><stop offset="0" stop-color="#3a2a24"/><stop offset=".45" stop-color="#efe9ea"/><stop offset="1" stop-color="#6b5146"/></linearGradient>
    <symbol id="waveBands" viewBox="0 0 285 285">
      <path d="M0 252 C70 270 160 238 285 244 L285 285 L0 285Z" fill="url(#purpleBand)"/>
      <path d="M0 205 C25 232 80 246 160 242 C110 252 50 258 0 254Z" fill="url(#blueBand)"/>
      <path d="M285 226 C235 228 195 238 150 246 C205 244 250 246 285 246Z" fill="url(#redBand)"/>
      <path d="M0 250 C70 268 150 246 285 240 L285 248 C160 252 80 276 0 262Z" fill="#fff"/>
    </symbol>
    <symbol id="tick" viewBox="0 0 10 10">
      <circle cx="5" cy="5" r="4.4" fill="none" stroke="#d42a3a" stroke-width="1"/>
      <path d="M2.8 5.2 L4.5 6.8 L8.6 1.8" fill="none" stroke="#d42a3a" stroke-width="1.6" stroke-linecap="round"/>
    </symbol>
  </defs>
</svg>

<section class="ad ad--1">
  <h2 class="headline">Burn Belly Fat Fast:<br>The 3-Part Solution<br>You Need Now!</h2>
  <div class="bottles" role="img" aria-label="Golden Meadow Kit three-bottle bundle"></div>
  <div class="photo photo--before-after-a" role="img" aria-label="Customer before and after photo"></div>
  <ul class="bullets bullets--list">
    <li><span class="icon icon--blue"></span>Melt stubborn belly fat</li>
    <li><span class="icon icon--pink"></span>Reduce bloating and inflammation</li>
    <li><span class="icon icon--red"></span>Get that waistline snatched</li>
    <li><span class="icon icon--blue"></span>Boost energy and confidence</li>
  </ul>
  <svg class="wave"><use href="#waveBands"/></svg>
</section>

<section class="ad ad--2">
  <h2 class="headline">Double Your<br>Weight Loss With<br>this Powerful Trio!</h2>
  <div class="bottles bottles--low" role="img" aria-label="Golden Meadow Kit three-bottle bundle"></div>
  <div class="photo photo--before-after-b" role="img" aria-label="Customer before and after photo"></div>
  <ul class="bullets bullets--grid">
    <li><span class="icon icon--blue"></span>Melt stubborn belly fat</li>
    <li><span class="icon icon--pink"></span>Reduce bloating and inflammation</li>
    <li><span class="icon icon--red"></span>Get that waistline snatched</li>
    <li><span class="icon icon--blue"></span>Boost energy and confidence</li>
  </ul>
  <svg class="wave"><use href="#waveBands"/></svg>
</section>

<section class="ad ad--3">
  <h2 class="headline">Lose Weight Naturally:<br>Ditch the Prescription<br>Pills &amp; Needles!</h2>
  <div class="bottles bottles--low" role="img" aria-label="Golden Meadow Kit three-bottle bundle"></div>
  <div class="photo photo--waist" role="img" aria-label="Slim waist with measuring tape"></div>
  <ul class="bullets bullets--grid">
    <li><span class="icon icon--blue"></span>Melt stubborn belly fat</li>
    <li><span class="icon icon--pink"></span>Reduce bloating and inflammation</li>
    <li><span class="icon icon--red"></span>Get that waistline snatched</li>
    <li><span class="icon icon--blue"></span>Boost energy and confidence</li>
  </ul>
  <svg class="wave"><use href="#waveBands"/></svg>
</section>

<section class="ad ad--4">
  <h2 class="headline">Tired of Stubborn Belly<br>Fat? Discover the Trio<br>That Works!</h2>
  <div class="bottles bottles--low" role="img" aria-label="Golden Meadow Kit three-bottle bundle"></div>
  <div class="photo photo--fitness" role="img" aria-label="Smiling fit woman in sportswear"></div>
  <ul class="bullets bullets--grid">
    <li><svg class="tick"><use href="#tick"/></svg>Melt stubborn belly fat</li>
    <li><svg class="tick"><use href="#tick"/></svg>Reduce bloating and inflammation</li>
    <li><svg class="tick"><use href="#tick"/></svg>Get that waistline snatched</li>
    <li><svg class="tick"><use href="#tick"/></svg>Boost energy and confidence</li>
  </ul>
  <svg class="wave"><use href="#waveBands"/></svg>
</section>

<section class="ad ad--5">
  <h2 class="headline headline--tall">Melt Away<br>Belly Fat<br>Faster<br>with This<br>Powerful<br>Trio!</h2>
  <svg class="feature" viewBox="0 0 285 285" role="img" aria-label="Woman presenting the three bottles of the kit">
    <circle cx="208" cy="150" r="75" fill="none" stroke="var(--ring)" stroke-width="1"/>
    <path d="M178 18 H238 V80 A72 72 0 1 1 178 80Z" fill="url(#skin)"/>
  </svg>
  <svg class="wave"><use href="#waveBands"/></svg>
</section>

<section class="ad ad--6">
  <h2 class="headline">Struggling to Lose<br>Weight? Discover Our<br>Ultimate Solution!</h2>
  <div class="bottles bottles--low" role="img" aria-label="Golden Meadow Kit three-bottle bundle"></div>
  <div class="photo photo--before-after-c" role="img" aria-label="Customer before and after photo"></div>
  <ul class="bullets bullets--grid">
    <li><svg class="tick"><use href="#tick"/></svg>Melt stubborn belly fat</li>
    <li><svg class="tick"><use href="#tick"/></svg>Reduce bloating and inflammation</li>
    <li><svg class="tick"><use href="#tick"/></svg>Get that waistline snatched</li>
    <li><svg class="tick"><use href="#tick"/></svg>Boost energy and confidence</li>
  </ul>
  <svg class="wave"><use href="#waveBands"/></svg>
</section>

<section class="ad ad--7">
  <h2 class="headline headline--compact">Ready to<br>Burn Fat<br>Faster?<br>Discover<br>the<br>Golden<br>Meadow<br>Kit!</h2>
  <svg class="feature" viewBox="0 0 285 285" role="img" aria-label="Woman presenting the three bottles of the kit">
    <circle cx="207" cy="150" r="75" fill="none" stroke="var(--ring)" stroke-width="1"/>
    <path d="M177 18 H237 V80 A72 72 0 1 1 177 80Z" fill="url(#skin)"/>
  </svg>
  <svg class="wave"><use href="#waveBands"/></svg>
</section>

</body>
</html>
```